BRIGHT COLORFUL + 55 FAMILY HISTORY BROCHURE 11 x 17 bifold

11 x 17 Bifold Flyer I have given you the Layout I just need you to make it Pretty

YOU DO NOT NEED TO FOLLOW MY LAYOUT, You can but dont have too

Target Market(s)

55 year old consumers, who could choose our service of Hereditary Cancer Screening

Industry/Entity Type

Health And Wellness

Requirements
Must have
• Must be appealing to Grand Parents, must make them want to test , show lots of pictures of grand children, YOU DO NOT NEED TO FOLLOW MY LAYOUT , You can but dont have too
Nice to have
• use our colors of our logo , YOU DO NOT NEED TO FOLLOW MY LAYOUT , You can but dont have too
Should not have
• YOU DO NOT NEED TO FOLLOW MY LAYOUT, You can but dont have too

```html
<!DOCTYPE html>
<html lang="en">
<head>
<meta charset="utf-8">
<title>Family History Cancer Screening Brochure</title>
<link rel="stylesheet" href="https://fonts.googleapis.com/css2?family=Open+Sans:ital,wght@0,400;0,700;1,700&family=Noto+Serif:wght@700&display=swap">
<style>
  :root {
    --backdrop: #5fcf5f;
    --paper: #f3f3f3;
    --navy: #2b3a6d;
    --ink: #3a3a3a;
    --green: #5fb84d;
    --fold: #d9d9d9;
    --photo-warm: #e6c9b4;
    --photo-soft: #cfc4bc;
    --photo-leaf: #9fb48a;
  }
  * { box-sizing: border-box; margin: 0; padding: 0; }
  html, body {
    width: 1200px; height: 1200px; overflow: hidden;
    background: var(--backdrop);
    font-family: "Open Sans", Arial, sans-serif;
    color: var(--ink);
  }
  .spread {
    position: absolute; left: 30px; top: 187px;
    width: 1140px; height: 826px;
    display: flex;
    background: var(--paper);
    box-shadow: 0 6px 18px rgba(0,0,0,.18);
  }
  .page { position: relative; width: 570px; height: 100%; }
  .page--left { padding: 62px 22px 0 22px; border-right: 1px solid var(--fold); }
  .page--right { padding: 56px 20px 0 16px; }

  .story { font-size: 13.3px; line-height: 17px; margin-bottom: 6px; }
  .story b { color: var(--navy); font-weight: 700; }
  .family-band {
    height: 128px; margin: 8px 0 12px;
    background: linear-gradient(90deg, #8fa7c4, #e8d2c0 35%, #d9b7c0 60%, #b9d1e6);
  }
  .story + .story.gap { margin-top: 10px; }

  .headline-serif {
    font-family: "Noto Serif", Georgia, serif; font-weight: 700;
    color: var(--navy); font-size: 19px; line-height: 25px;
    text-align: center; margin-top: 10px;
  }
  .note-green {
    font-weight: 700; font-style: italic; color: var(--green);
    font-size: 18.5px; line-height: 23px; text-align: center; margin-top: 6px;
  }

  .photo-column { float: left; width: 232px; margin-right: 24px; }
  .photo { height: 157px; margin-bottom: 15px; }
  .photo--baby { background: linear-gradient(135deg, var(--photo-soft), var(--photo-warm)); }
  .photo--trio { background: linear-gradient(135deg, #b9c6cf, var(--photo-warm) 60%, #c9b8a8); }
  .photo--hug { background: linear-gradient(135deg, var(--photo-leaf), #b8b8b0 60%, #8e9a86); margin-bottom: 0; }

  .info { font-size: 15.3px; line-height: 19.6px; }
  .info p { margin-bottom: 4px; }
  .info b { color: var(--navy); font-weight: 700; }
  .tagline {
    clear: both; font-weight: 700; font-style: italic; color: var(--green);
    font-size: 18px; line-height: 24px; text-align: center; padding-top: 16px;
  }
  .site {
    display: block; width: max-content; margin: 14px auto 0;
    background: var(--navy); color: #fff; font-style: italic;
    font-size: 13px; padding: 1px 4px;
  }
</style>
</head>
<body>
  <main class="spread">
    <section class="page page--left">
      <p class="story"><b>Genetic testing revealed</b> Martin Feldman carried a mutation that gave him a 55 to 70 percent chance of developing stomach cancer. Early screening revealed there were 14 sites of stage 1A cancer. Once the news sunk in, he realized <b>his Mother Genetic Testing Saved His Life.</b></p>
      <p class="story"><b>Genetic Testing Saved My Life,</b> Because of my age and Ashkenazi Jewish ancestry, My Dr recommended Genetic Testing and they were right. I had the BRCA Gene, because of this my other two sister got tested, my younger sister was positive and my older sister was negative. Now we are in control, there are steps that can be taken to reduce the risks, including enhanced breast cancer screening, risk-reducing surgeries, and chemoprevention, in which drugs are used to try to reduce the risk or delay the development of cancer.</p>
      <div class="family-band" role="img" aria-label="Photo of three generations of a smiling family with grandparents and grandchildren"></div>
      <p class="story"><b>A breast cancer survivor before age 30:</b> ‘Genetic testing saved my life’ Carla Hughes was diagnosed with breast cancer two weeks before her 29th birthday. Hughes, now 30, credits her recovery to awareness of a hereditary genetic mutation that predisposed her and her family to the disease. After my mom tested positive for the BRCA 1 gene mutation, I knew genetic testing was something that I would need. Once I tested positive, I was referred to a breast health clinic for increased surveillance. There, my medical care providers were very diligent in making sure I was watched closely. Knowledge is power and, in this case, Genetic testing saved my life !</p>
      <p class="story gap"><b>My father had genetic testing</b> and found he had hereditary nonpolyposis colorectal cancer (HNPCC) commonly known as Lynch syndrome. My name is Diane Morrow and I am a 10-year survivor of colorectal cancer. From an early age I learned the importance of screenings and knew about signs and symptoms. Followin screening guidelines for individuals at an increased risk &amp; Knowing my family history saved my life !</p>
      <p class="headline-serif">learning if you have an increased risk for cancer can make a difference.</p>
      <p class="note-green">A Positive result or finding a mutation is Not a Cancer Diagnosis and does not mean you will ever develop Cancer</p>
    </section>

    <section class="page page--right">
      <div class="photo-column">
        <div class="photo photo--baby" role="img" aria-label="Photo of a grandmother and mother with a sleeping newborn"></div>
        <div class="photo photo--trio" role="img" aria-label="Photo of grandparents hugging their granddaughter"></div>
        <div class="photo photo--hug" role="img" aria-label="Photo of a grandfather embracing his young grandson outdoors"></div>
      </div>
      <div class="info">
        <p><b>Genetic Testing</b> is done to determine whether family members without obvious illness have inherited the same mutation as a family member who is known to carry a cancer associated mutation. Meaning <b>Will You Help Your Kids &amp; Grand Children.</b></p>
        <p><b>What are the benefits of testing?</b> “The Power of Knowledge” Helping Younger Family Members Know if there is a Risk and Preparing for it. knowing if you have a genetic mutation is that you can work with your doctor to monitor and address your cancer risks. According to the National Wellness Council eating 5 or more Servings of Vegetables &amp; Fruit, and <b>Most Importantly also lowering your intake of red meat, dairy and eggs will help prevent or delay cancer.</b></p>
        <p><b>There are many benefits to getting tested,</b> regardless of the eventual result. If one of your family members — however distant — had cancer, there is a chance that you inherited a gene mutation that not only increase your personal risk of cancer, but also could be passed to the next generation. Those who are carriers of hereditary cancer gene mutations, could be at risk of getting cancer earlier in life than the general population. The sooner genetic testing is done, <b>The more likely it is that the risk can be managed appropriately.</b></p>
      </div>
      <p class="tagline">There are many Known risk factors for Cancer. GENETICS and FAMILY HISTORY are Often. Overlooked.</p>
      <span class="site">www.familyRiskCheck.com</span>
    </section>
  </main>
</body>
</html>
```